Business Card for Business consulting practice

Need a design for a consultant business card. Simple and elegant.
I need the following information on the card:
Logo: (see uploaded file)
Company name: Calmora Advisory Group
Name: Dana Weltrup
Title: Managing Director - Aerospace and Defence
Phone #: 514-268-3917
e-mail: dana.weltrup@calmora-example.com
Website: www.calmora-example.com
Tagline: Proposals Management and Capture support for complex procurements

```html
<!DOCTYPE html>
<html lang="en">
<head>
<meta charset="utf-8">
<title>Calmora Advisory Group – Business Card</title>
<link href="https://fonts.googleapis.com/css2?family=Arimo:wght@400;700&display=swap" rel="stylesheet">
<style>
  :root {
    --sky: #0e97c3;
    --navy: #0b2d45;
    --white: #ffffff;
    --backdrop: #e9e9e9;
  }
  * { margin: 0; padding: 0; box-sizing: border-box; }
  html, body { width: 1200px; height: 802px; overflow: hidden; }
  body {
    background: var(--backdrop);
    font-family: "Arimo", Arial, sans-serif;
    color: var(--white);
    position: relative;
  }
  .card {
    position: absolute;
    width: 530px;
    height: 302px;
    border-radius: 3px;
    overflow: hidden;
    box-shadow: 0 10px 24px rgba(0,0,0,0.18);
  }
  /* Front side */
  .card-front { left: 45px; top: 250px; background: var(--sky); }
  .card-front .panel { position: absolute; inset: 0; }
  .front-content {
    position: absolute;
    left: 34px;
    top: 56px;
    width: 300px;
  }
  .brand-name {
    font-weight: 700;
    font-size: 20px;
    letter-spacing: 0.5px;
    padding-bottom: 8px;
    border-bottom: 1px solid rgba(255,255,255,0.8);
    display: inline-block;
  }
  .person-name {
    margin-top: 22px;
    font-weight: 700;
    font-size: 21px;
    text-transform: uppercase;
    letter-spacing: 0.3px;
  }
  .person-title {
    font-size: 14px;
    line-height: 1.3;
    margin-top: 4px;
  }
  .contact-list { list-style: none; margin-top: 20px; }
  .contact-list li {
    display: flex;
    align-items: center;
    gap: 9px;
    font-size: 14px;
    line-height: 1.55;
  }
  .contact-list svg { width: 12px; height: 12px; flex: none; }
  .mark-circle {
    position: absolute;
    right: 58px;
    top: 52px;
    width: 150px;
    height: 150px;
    border-radius: 50%;
    border: 10px solid var(--sky);
  }
  /* Back side */
  .card-back {
    left: 625px; top: 250px;
    background: var(--navy);
    display: flex;
    flex-direction: column;
    align-items: center;
    justify-content: center;
    text-align: center;
  }
  .back-brand {
    font-weight: 700;
    font-size: 30px;
    letter-spacing: 0.5px;
    padding: 0 18px 12px;
    border-bottom: 1px solid var(--sky);
  }
  .tagline {
    margin-top: 34px;
    font-size: 15px;
    line-height: 1.4;
  }
</style>
</head>
<body>

  <section class="card card-front" aria-label="Business card front">
    <svg class="panel" viewBox="0 0 530 302" preserveAspectRatio="none" aria-hidden="true">
      <polygon points="300,0 530,0 530,302 390,302" fill="var(--navy)"/>
    </svg>
    <div class="mark-circle" aria-hidden="true"></div>
    <div class="front-content">
      <div class="brand-name">Calmora Advisory Group</div>
      <h1 class="person-name">Dana Weltrup</h1>
      <p class="person-title">Managing Director<br>Aerospace and Defence</p>
      <ul class="contact-list">
        <li>
          <svg viewBox="0 0 24 24" aria-hidden="true"><path fill="#fff" d="M6.6 10.8a15.1 15.1 0 0 0 6.6 6.6l2.2-2.2c.3-.3.7-.4 1-.2 1.1.4 2.3.6 3.6.6.6 0 1 .4 1 1V20c0 .6-.4 1-1 1A17 17 0 0 1 3 4c0-.6.4-1 1-1h3.5c.6 0 1 .4 1 1 0 1.3.2 2.5.6 3.6.1.3 0 .7-.2 1z"/></svg>
          514-268-3917
        </li>
        <li>
          <svg viewBox="0 0 24 24" aria-hidden="true"><path fill="#fff" d="M2 5h20v14H2zm2 2v.5l8 5 8-5V7l-8 5z"/></svg>
          dana.weltrup@calmora-example.com
        </li>
        <li>
          <svg viewBox="0 0 24 24" aria-hidden="true"><circle cx="12" cy="12" r="10" fill="none" stroke="#fff" stroke-width="2"/><path d="M2 12h20M12 2c3 3 3 17 0 20M12 2c-3 3-3 17 0 20" fill="none" stroke="#fff" stroke-width="1.6"/></svg>
          www.calmora-example.com
        </li>
      </ul>
    </div>
  </section>

  <section class="card card-back" aria-label="Business card back">
    <div class="back-brand">Calmora Advisory Group</div>
    <p class="tagline">Proposals Management And<br>Capture Support For Complex Procurements</p>
  </section>

</body>
</html>
```